Business Card Project for 'Manufacturing and Healthcare Business Improvement company.

I need a business card for a consulting company that does process improvement for manufacturing and healthcare companies. I had a contest for a logo, and I liked what we came up with for the logo.

I wasn't blown away by what I got for the business card. The designer tried and it was a decent design, but I was looking for a little more. I want something that looks professional, but is eye-catching enough that people say "that looks cool, where did you get it?"

I've uploaded some business card examples I found that I liked. Even though some of the examples have red and orange on them, I think I would stick with blues, grays and blacks since that matches the logo theme. As awesome as some of them look, I don't think that a single color card, like an all-black card, will work for me; but feel free to change my mind.

It might also be possible to incorporate elements from the logo into the card. I also like some of the elements that use circles or rectangles etc to separate the phone number, website etc.

I like it when people have used geometric shapes to break up the card into sections or to add borders to the card to complement the logo, not compete with it for attention. For example, the red and gray example that has a curve that separates the card into two parts. I've wondered, how it would look if the red area were blue and had an arrow separating the top and bottom, like the arrow on the logo. Maybe on the back there could be an element that mirrors the bar graph and arrow. Would those look interesting, or would they compete with the other elements too much?

I also uploaded some examples of cards I made up, either based on ideas I saw elsewhere or based on design elements that the logo had in his designs. If you wonder why the ones with "lorem ipsum" look like an amateur did them, it's because they did.

I also think that I may add a QR code at some point, so I would need a location for that, along with something that says what the QR links to, such as, "scan here to upload contact information" or something similar. I don't know if I want cards that require having special designs cut, but if you have the idea, go with it.

I don't want to limit anyone's creativity, so I'll leave it at that.

Target Market(s)

Healthcare and Manufacturing

Industry/Entity Type

Manufacturing

Contact Information for Business Card

Harborline Advisory Group LLC.
Owen Prescott MBA, LSSMBB
Managing Partner
o.prescott@harborlineadvisorygroupllc.com
(555) 987-2310

Font styles to use
Serif
Sans Serif

Colors

Designer to choose only greyscale colors for use in the design.

Requirements
Must have
• The logo.
Nice to have
• Even though some of the examples I uploaded have red and orange on them, I think I would stick with blues, grays and blacks since that matches the logo theme.

I also like some of the elements that use circles or rectangles etc to separate the phone number, website etc.

I like it when people have used geometric shapes to break up the card into sections or to add borders to the card to complement the logo, not compete with it for attention.

For example, the red and gray example that has a curve that separates the card into two parts. I've wondered, how it would look if the red area were blue and had an arrow separating the top and bottom, like the arrow on the logo. Maybe on the back there could be an element that mirrors the bar graph and arrow. Would those look interesting, or would they compete with the other elements too much?

It might also be possible to incorporate elements from the logo into the card.

I also think that I may add a QR code at some point, so I would need a location for that, along with something that says what the QR links to, such as, "scan here to upload contact information" or something similar.

It could have something somewhere saying "We use Lean, Six Sigma and TPM continuous improvement tools to improve manufacturing and healthcare businesses."
Should not have
• So many colors and elements that it is distracting. Should not be generic.

As awesome as some of them look, I don't think that a single color card, like an all-black card, will work for me; but feel free to change my mind.

I don't know if I want cards that require having special designs cut, but if you have the idea, go with it.

```html
<!DOCTYPE html>
<html lang="en">
<head>
<meta charset="utf-8">
<title>Harborline Advisory Group – Business Card</title>
<link href="https://fonts.googleapis.com/css2?family=Lato:wght@400;700&display=swap" rel="stylesheet">
<style>
  :root {
    --stage: #2a2c30;
    --card: #ffffff;
    --border: #2b35a6;
    --navy: #1d3863;
    --ink: #1b1b1b;
    --muted: #3a3a3a;
  }
  * { box-sizing: border-box; margin: 0; padding: 0; }
  html, body { width: 1200px; height: 900px; overflow: hidden; }
  body {
    background: var(--stage);
    font-family: "Lato", Arial, sans-serif;
    display: flex;
    align-items: center;
    justify-content: center;
    gap: 40px;
  }
  .card {
    position: relative;
    width: 540px;
    height: 309px;
    background: var(--card);
    border: 7px solid var(--border);
    overflow: hidden;
  }

  /* Contact side */
  .brand-small {
    position: absolute;
    top: 26px;
    left: 28px;
    display: flex;
    align-items: center;
    gap: 8px;
    color: var(--navy);
    font-weight: 700;
    font-size: 13px;
    letter-spacing: 0.02em;
  }
  .brand-square { width: 14px; height: 14px; background: var(--navy); flex: none; }
  .contact-list {
    position: absolute;
    top: 70px;
    left: 28px;
    list-style: none;
    font-size: 12.5px;
    color: var(--ink);
  }
  .contact-list li {
    display: flex;
    align-items: center;
    gap: 9px;
    margin-bottom: 9px;
  }
  .contact-list svg { width: 14px; height: 14px; fill: var(--navy); flex: none; }
  .divider {
    position: absolute;
    top: 150px;
    left: 28px;
    width: 214px;
    height: 2px;
    background: var(--navy);
  }
  .person {
    position: absolute;
    top: 139px;
    left: 252px;
    width: 250px;
  }
  .person-name {
    color: var(--navy);
    font-size: 17px;
    font-weight: 400;
    white-space: nowrap;
  }
  .person-role,
  .person-company {
    color: var(--muted);
    font-size: 11.5px;
    white-space: nowrap;
  }
  .person-role { text-align: right; margin-top: 3px; }
  .person-company { margin-top: 2px; }
  .corner-accent {
    position: absolute;
    right: 28px;
    bottom: 26px;
    width: 40px;
    height: 40px;
    background: var(--navy);
  }

  /* Brand side */
  .card-back {
    display: flex;
    align-items: center;
    justify-content: center;
  }
  .brand-large {
    display: flex;
    align-items: center;
    gap: 14px;
    color: var(--navy);
    font-weight: 700;
    font-size: 26px;
    letter-spacing: 0.02em;
    white-space: nowrap;
  }
  .brand-large .brand-square { width: 26px; height: 26px; }
</style>
</head>
<body>
  <section class="card card-front" aria-label="Card contact side">
    <div class="brand-small"><span class="brand-square"></span>Harborline Advisory Group LLC</div>
    <ul class="contact-list">
      <li>
        <svg viewBox="0 0 24 24" aria-hidden="true"><path d="M6.6 10.8a15.1 15.1 0 0 0 6.6 6.6l2.2-2.2a1 1 0 0 1 1-.25 11.4 11.4 0 0 0 3.6.57 1 1 0 0 1 1 1V20a1 1 0 0 1-1 1A17 17 0 0 1 3 4a1 1 0 0 1 1-1h3.5a1 1 0 0 1 1 1c0 1.25.2 2.45.57 3.57a1 1 0 0 1-.25 1z"/></svg>
        (555) 987-2310
      </li>
      <li>
        <svg viewBox="0 0 24 24" aria-hidden="true"><path d="M2 5h20v14H2z M2 5l10 8 10-8" fill="none" stroke="#1d3863" stroke-width="2"/></svg>
        o.prescott@harborlineadvisorygroupllc.com
      </li>
    </ul>
    <div class="divider"></div>
    <div class="person">
      <p class="person-name">Owen Prescott MBA, LSSMBB</p>
      <p class="person-role">Managing Partner</p>
      <p class="person-company">Harborline Advisory Group LLC.</p>
    </div>
    <div class="corner-accent" aria-hidden="true"></div>
  </section>

  <section class="card card-back" aria-label="Card brand side">
    <div class="brand-large"><span class="brand-square"></span>Harborline Advisory Group LLC</div>
  </section>
</body>
</html>
```